Harvesting the Eastern Ledger - book cover design

I need a cover designed for a new book (paperback and eBook).
The title is: “Harvesting the Eastern Ledger” with the subtitle: “The single guide required to begin building gains with Asian equities”. It is from the first time author :“Teemu Halvorsen“.
The following text should also be visible in the front cover: “From the founder of PandoraQuayFund.com” or "Founder of PandoraQuayFund.com".
The publisher’s logo, should also be visible somewhere on the cover (front, back or spine). The logo, along with source files are here: http://qvfiles.example/7TrwmpK
The book/paperback cover dimensions are: 5.06 x 7.81 inches (12.9 x 19.8 centimeters). Here are the book-cover templates recommended by Brindlebook for a book of this size:
http://qvfiles.example/9GdLs2W (.indd)
http://qvfiles.example/4NbZuoH (.pdf)
Below is a description of the book. I don't have a specific idea or vision in mind for the cover. I'd like to see what designs and ideas SketchHarbor designers come up with.
Color red is usually associated with China, but I don’t want the book to be red. Instead the background color could be one of the publisher’s brand colors (#88C198, #017487). However I’ll leave you the designers freedom to propose any colors and combinations.
This is not an entry level book, but a very advanced level investment strategy book for international investors. It explains with concrete examples how non-Chinese citizens can best benefit from China’s economic miracle by picking the best Chinese growth stocks from New York, Hong Kong and Singapore stock exchanges.
The book cover should not have dollar signs promising easy and fast money (because easy and fast money doesn’t exist). What the book promises is a very advanced level China investing strategy, which will considerably improve international investors’ odds for big profits in the longer term.
The big investment themes in the book are China’s consumer sector and service industries.
The book cover should have some kind of reference/association to Investing and China.
The design needs to work and be effective at both a large book cover size and a small thumbnail-sized image - the way that many people browse book covers on Brindlebook and other websites. Therefore, a design that relies on really small details probably won't translate at the smaller image sizes that book covers are displayed online.
Target Market(s)
International investors (~50% from western countries, 30% from Singapore/Hong Kong, Malaysia)
Industry/Entity Type
Investment
Font styles to use
Other font styles liked:
- EB Garamond, Grimson text or some other beautiful book font
Look and feel

```html
<!DOCTYPE html>
<html lang="en">
<head>
<meta charset="utf-8">
<title>Harvesting the Eastern Ledger — Book Cover</title>
<link rel="stylesheet" href="https://fonts.googleapis.com/css2?family=Josefin+Sans:wght@300;400&family=Lato:ital,wght@1,300&family=Pacifico&family=Questrial&display=swap">
<style>
  :root {
    --backdrop: #ececec;
    --cover: #ffffff;
    --title-red: #b81f2d;
    --accent-gold: #f5b800;
    --muted-grey: #55585c;
    --author-brown: #3b2c2c;
    --brand-teal: #017487;
  }
  * { box-sizing: border-box; margin: 0; padding: 0; }
  html, body {
    width: 946px; height: 1200px; overflow: hidden;
    background: var(--backdrop);
  }
  .cover {
    position: absolute;
    left: 116px; top: 50px;
    width: 714px; height: 1100px;
    background: var(--cover);
    box-shadow: 0 6px 24px rgba(0,0,0,0.12);
  }
  .founder-line {
    position: absolute; top: 88px; left: 0; right: 0;
    text-align: center;
    font-family: "Lato", sans-serif; font-style: italic; font-weight: 300;
    font-size: 27px; letter-spacing: 1px;
    color: var(--muted-grey);
  }
  .title {
    position: absolute; top: 250px; left: 0; right: 0;
    text-align: center;
    font-family: "Josefin Sans", sans-serif; font-weight: 400;
    color: var(--title-red);
    line-height: 1;
  }
  .title-line { display: block; }
  .title-line--first { font-size: 92px; letter-spacing: 1px; }
  .title-line--middle { font-size: 100px; margin-top: 22px; }
  .title-line--last { font-size: 150px; margin-top: 18px; }
  .title-script {
    font-family: "Pacifico", cursive;
    font-size: 34px; letter-spacing: 0;
    vertical-align: middle;
    margin-right: 6px;
    position: relative; top: -8px;
  }
  .emblem-placeholder {
    position: absolute; top: 735px; left: 50%;
    width: 84px; height: 84px;
    transform: translateX(-50%);
    border-radius: 50%;
    background: radial-gradient(circle at 40% 40%, #f9cf4a, var(--accent-gold));
  }
  .subtitle {
    position: absolute; top: 850px; left: 150px; right: 150px;
    text-align: center;
    font-family: "Questrial", sans-serif;
    font-size: 25px; line-height: 1.25; letter-spacing: 0.8px;
    color: var(--muted-grey);
  }
  .imprint {
    position: absolute; bottom: 62px; left: 56px; right: 44px;
    display: flex; align-items: center; justify-content: space-between;
  }
  .publisher {
    display: flex; align-items: center; gap: 8px;
    font-family: "Josefin Sans", sans-serif; font-weight: 400;
    font-size: 18px; letter-spacing: 1px;
    color: var(--brand-teal);
  }
  .publisher-dot {
    width: 14px; height: 14px; border-radius: 50%;
    background: var(--brand-teal);
  }
  .author {
    font-family: "Josefin Sans", sans-serif; font-weight: 400;
    font-size: 38px; letter-spacing: 4px;
    color: var(--author-brown);
  }
</style>
</head>
<body>
  <main class="cover">
    <p class="founder-line">From the founder of PandoraQuayFund.com</p>

    <h1 class="title">
      <span class="title-line title-line--first">HARVESTING</span>
      <span class="title-line title-line--middle"><span class="title-script">the</span>EASTERN</span>
      <span class="title-line title-line--last">LEDGER</span>
    </h1>

    <div class="emblem-placeholder" role="img" aria-label="Small gold emblem motif"></div>

    <p class="subtitle">The single guide required to begin building gains with Asian equities</p>

    <footer class="imprint">
      <div class="publisher"><span class="publisher-dot"></span>Quayside</div>
      <p class="author">TEEMU HALVORSEN</p>
    </footer>
  </main>
</body>
</html>
```